VornaDerm/The experts in permanent hairremoval

Our Brand is VornaDerm and we are specialized on permantent hair removal for the body for men and woman. VornaDerm is working as a Franchise chain.
The brand should be positioned as lifestyle brand but with a medical background. People should trust in us. We take care about their body. This need to be communicated 100%.
Our system is inexpensive but we don't want to show that we are cheap. So we want to communicate that permanent hair removal is a real lifestyle product but affordable.
We already created a logo that you can see the style and colour we prefer.

Target Market(s)

Europe beginning (especially german spoken markets), Middle East, Africa

Industry/Entity Type

Hair Removal

Number of Pages Required

5+ page

Font styles to use
Serif
Other font styles liked:
• Trajan Pro

Requirements
Nice to have
• We are very open for new ideas

```html
<!DOCTYPE html>
<html lang="en">
<head>
<meta charset="utf-8">
<title>VornaDerm – Laser Skin Renewal</title>
<link href="https://fonts.googleapis.com/css2?family=Roboto:wght@300;400;500;700&family=Open+Sans:wght@400;600&display=swap" rel="stylesheet">
<style>
:root{
  --blue:#3a98d8;
  --blue-dark:#2b7fc0;
  --ink:#3a3a3a;
  --text:#2c2c2c;
  --muted:#6c6c6c;
  --dark:#2e2f31;
  --field:#d6d6d6;
  --paper:#f1f1f1;
  --white:#ffffff;
}
*{margin:0;padding:0;box-sizing:border-box}
html,body{width:960px;height:1200px;overflow:hidden}
body{font-family:"Open Sans",Arial,sans-serif;color:var(--text);background:var(--paper)}
.page{position:relative;width:960px;height:1200px;overflow:hidden;background:linear-gradient(180deg,#f4f4f4 0%,#ebebeb 60%,#e4e4e4 100%)}
.abs{position:absolute}
.backdrop{position:absolute;left:0;top:0}

/* top navigation */
.main-nav{position:absolute;left:248px;top:10px;display:flex;gap:13px;font-family:"Roboto",sans-serif;font-size:8px;color:var(--white);letter-spacing:.2px}
.contact-line{position:absolute;left:300px;top:37px;font-family:"Open Sans",sans-serif;font-size:7.4px;color:var(--white);display:flex;align-items:center;gap:5px}
.contact-line b{font-weight:600}
.social-dots{display:flex;gap:3px;margin-left:5px}
.social-dots span{width:13px;height:13px;border-radius:50%;background:var(--white);display:block}

/* brand */
.brand{position:absolute;left:594px;top:12px;display:flex;align-items:center;gap:8px}
.brand-dot{width:30px;height:30px;border-radius:50%;background:var(--blue)}
.brand-name{font-family:"Roboto",sans-serif;font-weight:400;font-size:30px;color:#6e6e6e;line-height:1}
.brand-tag{position:absolute;left:636px;top:48px;font-family:"Roboto",sans-serif;font-size:5.2px;color:#6e6e6e;letter-spacing:.3px}

/* hero */
.hero-bubble{position:absolute;left:502px;top:110px;width:184px;height:184px;border-radius:50%;background:radial-gradient(circle at 40% 35%,#4aa6e2,#2f88cb);border:4px solid #fff;box-shadow:0 6px 14px rgba(0,0,0,.25);display:flex;align-items:center;padding-left:30px}
.hero-bubble h1{font-family:"Roboto",sans-serif;font-weight:300;font-size:19.5px;line-height:20px;color:var(--white)}

/* intro */
.intro{position:absolute;left:268px;top:364px;width:326px}
.intro h2{font-family:"Roboto",sans-serif;font-weight:300;font-size:13.5px;color:var(--ink);margin-bottom:10px}
.intro p{font-size:6.9px;line-height:9.6px;margin-bottom:9px;color:var(--text)}
.intro p a{color:#4c4cc4}
.topic-links{list-style:none;margin-top:4px}
.topic-links li{font-size:7.4px;line-height:12px}
.topic-links a{color:var(--blue)}

.section-title{position:absolute;font-family:"Roboto",sans-serif;font-weight:300;font-size:13.5px;color:var(--ink)}

/* special */
.special{position:absolute;left:254px;top:587px;width:451px;height:77px;background:linear-gradient(180deg,#d9dde2,#bfc6cf);border:1px solid #a9b0b8;box-shadow:0 3px 6px rgba(0,0,0,.25)}
.special-lead{position:absolute;left:118px;top:8px;width:122px}
.special-lead h3{font-family:"Roboto",sans-serif;font-weight:400;font-size:11.5px;line-height:13px;color:var(--blue)}
.special-lead p{font-family:"Roboto",sans-serif;font-size:7px;line-height:8.6px;color:#333;margin-top:4px}
.deal{position:absolute;top:0;width:66px;text-align:center;font-family:"Roboto",sans-serif}
.deal .count{position:absolute;left:17px;top:-17px;width:32px;height:32px;border-radius:50%;background:var(--blue);border:3px solid #fff;color:#fff;font-weight:500;font-size:13px;line-height:26px;box-shadow:0 2px 4px rgba(0,0,0,.25)}
.deal .price{margin-top:26px;font-size:13px;font-weight:500;color:var(--blue)}
.deal .label{font-size:8.6px;line-height:9.6px;color:#222;margin-top:2px}
.special-call{position:absolute;left:254px;top:671px;width:451px;text-align:center;font-family:"Roboto",sans-serif;font-size:9px;color:var(--blue)}
.special-call b{font-weight:700}
.special-note{position:absolute;left:254px;top:684px;width:451px;text-align:center;font-family:"Roboto",sans-serif;font-size:7px;color:#222}

/* blog */
.blog-arrow{position:absolute;top:752px}
.post{position:absolute;top:728px;width:144px;text-align:center}
.post-image{width:144px;height:78px;position:relative}
.post-date{position:absolute;right:6px;top:6px;width:30px;height:40px;background:#fff;box-shadow:0 1px 3px rgba(0,0,0,.3);font-family:"Roboto",sans-serif;color:var(--blue);text-align:center;font-weight:500}
.post-date span{display:block;font-size:6.5px;margin-top:4px}
.post-date strong{display:block;font-size:13px;line-height:12px}
.post h4{font-family:"Roboto",sans-serif;font-weight:400;font-size:7.8px;line-height:9.4px;color:var(--blue);margin:10px 6px 0}
.post p{font-family:"Roboto",sans-serif;font-size:6.6px;line-height:8.4px;color:#333;margin:8px 6px 0}
.read-more{display:inline-block;margin-top:9px;width:57px;height:13px;line-height:13px;background:var(--blue);color:#fff;font-family:"Roboto",sans-serif;font-size:6.4px}

/* appointment */
.appointment-head{position:absolute;right:532px;top:916px;text-align:right;font-family:"Roboto",sans-serif;color:var(--blue);font-weight:300}
.appointment-head .small{font-size:14px;line-height:13px}
.appointment-head .big{font-size:18.5px;line-height:18px}
.appointment-head p{font-family:"Roboto",sans-serif;font-size:7px;line-height:9.6px;color:#222;font-weight:400;margin-top:4px}
.booking{position:absolute;left:256px;top:990px;width:173px;height:204px;background:#fff}
.field{position:absolute;left:5px;width:163px;height:21px;background:var(--field);font-family:"Roboto",sans-serif;font-size:6.5px;color:#555;padding:6px 0 0 8px}
.book-btn{position:absolute;left:5px;top:178px;width:70px;height:18px;background:var(--blue);color:#fff;font-family:"Roboto",sans-serif;font-size:6.5px;line-height:18px;padding-left:11px}

/* newsletter */
.newsletter{position:absolute;right:260px;top:1038px;text-align:right;color:#fff;font-family:"Roboto",sans-serif;font-weight:300}
.newsletter p{font-size:8px;line-height:10.4px;color:#eee;font-weight:400}
.newsletter .join{font-size:13px;line-height:13px;margin-top:9px}
.newsletter .title{font-size:18.5px;line-height:18px}
.link-us{position:absolute;left:533px;top:1126px;display:flex;align-items:center;gap:7px;color:#fff;font-family:"Roboto",sans-serif;font-weight:300;font-size:11.5px}
.link-us i{display:block;width:24px;height:24px;border-radius:50%;background:#5aa9de;border:2px solid #d8ecf8}
.link-us span{margin-right:12px}
.footer-nav{position:absolute;left:455px;top:1170px;font-family:"Roboto",sans-serif;font-size:6.2px;color:#fff}
.footer-copy{position:absolute;left:455px;top:1180px;font-family:"Roboto",sans-serif;font-size:5.4px;color:#ccc}
</style>
</head>
<body>
<div class="page">

  <svg class="backdrop" width="960" height="1200" viewBox="0 0 960 1200">
    <defs>
      <linearGradient id="skinWarm" x1="0" y1="0" x2="1" y2="1">
        <stop offset="0" stop-color="#b99683"/><stop offset=".55" stop-color="#e2c1aa"/><stop offset="1" stop-color="#f2ddcd"/>
      </linearGradient>
      <linearGradient id="fadedGrey" x1="0" y1="0" x2="1" y2="1">
        <stop offset="0" stop-color="#f3f3f3"/><stop offset=".5" stop-color="#dcdcdc"/><stop offset="1" stop-color="#efefef"/>
      </linearGradient>
      <linearGradient id="darkWedge" x1="0" y1="0" x2="0" y2="1">
        <stop offset="0" stop-color="#1f2022"/><stop offset="1" stop-color="#505256"/>
      </linearGradient>
      <linearGradient id="portrait" x1="0" y1="0" x2="1" y2="1">
        <stop offset="0" stop-color="#3b2e2a"/><stop offset=".45" stop-color="#cfa994"/><stop offset="1" stop-color="#f5ece6"/>
      </linearGradient>
      <linearGradient id="smile" x1="0" y1="0" x2="1" y2="1">
        <stop offset="0" stop-color="#c69c80"/><stop offset="1" stop-color="#f1d8c6"/>
      </linearGradient>
      <linearGradient id="bigRight" x1="0" y1="0" x2="0" y2="1">
        <stop offset="0" stop-color="#e7e9ec"/><stop offset=".35" stop-color="#d9b9a4"/><stop offset=".7" stop-color="#a68c80"/><stop offset="1" stop-color="#2e2f32"/>
      </linearGradient>
      <linearGradient id="blueFace" x1="0" y1="0" x2="1" y2="1">
        <stop offset="0" stop-color="#1f86cc"/><stop offset="1" stop-color="#7cc3ee"/>
      </linearGradient>
      <linearGradient id="seated" x1="0" y1="0" x2="0" y2="1">
        <stop offset="0" stop-color="#8a6a5b"/><stop offset=".4" stop-color="#e9d2c3"/><stop offset="1" stop-color="#f4eee9"/>
      </linearGradient>
      <linearGradient id="lotion" x1="0" y1="0" x2="0" y2="1">
        <stop offset="0" stop-color="#f7efe9"/><stop offset="1" stop-color="#e2c3ac"/>
      </linearGradient>
      <linearGradient id="spaPhoto" x1="0" y1="0" x2="1" y2="0">
        <stop offset="0" stop-color="#9aa3ac"/><stop offset="1" stop-color="#d9c1b0"/>
      </linearGradient>
    </defs>

    <polygon points="592,0 960,0 960,452" fill="url(#fadedGrey)" role="img" aria-label="Faded photo of a smiling woman touching her face"/>
    <polygon points="0,0 448,0 220,384 0,164" fill="url(#skinWarm)" role="img" aria-label="Close-up photo of a smiling woman"/>
    <polygon points="228,0 608,0 440,290 300,230" fill="url(#darkWedge)"/>
    <polygon points="236,0 604,0 590,30 228,30" fill="var(--blue)" opacity=".9"/>

    <circle cx="408" cy="204" r="139" fill="#fff"/>
    <circle cx="408" cy="204" r="134" fill="url(#portrait)" role="img" aria-label="Portrait photo of a dark-haired woman"/>

    <!-- intro photo frame -->
    <polygon points="600,360 680,360 680,366 606,366 606,440 600,440" fill="var(--dark)"/>
    <rect x="604" y="364" width="100" height="170" fill="url(#lotion)" role="img" aria-label="Photo of a woman applying cream to her shoulder"/>
    <polygon points="704,512 716,512 704,524" fill="var(--blue)"/>
    <polygon points="680,534 692,534 680,548" fill="var(--blue)"/>

    <!-- right smiling photo -->
    <polygon points="790,592 868,592 868,670" fill="var(--blue)"/>
    <polygon points="706,606 852,606 852,760" fill="url(#smile)" role="img" aria-label="Photo of a laughing woman"/>

    <!-- big lower right photo -->
    <polygon points="872,764 960,768 960,1200 414,1200" fill="url(#bigRight)" role="img" aria-label="Photo of a smiling blonde woman resting her face on her hand"/>
    <rect x="444" y="900" width="150" height="228" rx="60" fill="url(#seated)" opacity=".9" role="img" aria-label="Photo of a seated woman with long hair"/>

    <!-- lower left blue photo -->
    <polygon points="66,988 160,988 250,1080" fill="#b9d6ea"/>
    <polygon points="94,1000 250,1000 250,1156" fill="url(#blueFace)" role="img" aria-label="Blue-tinted photo of a woman looking up"/>

    <!-- booking frame -->
    <polygon points="420,986 434,986 434,1166 420,1180" fill="var(--dark)"/>
    <polygon points="252,986 434,986 428,992 252,992" fill="var(--dark)"/>

    <!-- special banner photo -->
    <rect x="255" y="588" width="110" height="76" fill="url(#spaPhoto)" role="img" aria-label="Photo of a woman receiving a laser skin treatment"/>

    <!-- blog images -->
    <rect x="254" y="728" width="144" height="78" fill="#e6c3b3" role="img" aria-label="Photo of lips and chin during a skin treatment"/>
    <rect x="407" y="728" width="144" height="78" fill="#7c7a6a" role="img" aria-label="Photo of a facial mask being applied"/>
    <rect x="561" y="728" width="144" height="78" fill="#8b7b74" role="img" aria-label="Photo of a dark-haired woman in profile"/>
  </svg>

  <nav class="main-nav">
    <span>HOME</span><span>STUDIOS</span><span>PRICES</span><span>ABOUT</span><span>JOBS</span><span>FRANCHISE</span><span>SHOP</span><span>CONTACT</span>
  </nav>
  <div class="contact-line">
    <span><b>Phone:</b> (000) 000-0000</span><span>|</span><span><b>Email:</b> info@vornaderm.com</span>
    <span class="social-dots"><span></span><span></span><span></span></span>
  </div>

  <div class="brand"><span class="brand-dot"></span><span class="brand-name">VornaDerm</span></div>
  <div class="brand-tag">THE EXPERTS IN PERMANENT HAIR REMOVAL</div>

  <div class="hero-bubble"><h1>Are there any<br>Side Effects of<br>Laser Skin<br>Renewal<br>Therapy?</h1></div>

  <section class="intro">
    <h2>Have you considered Laser Skin Renewal Therapy?</h2>
    <p>You will truly love laser skin renewal if your skin is showing signs of premature aging or the skin has sustained sun damage. Conditions such as excessive redness due to sun exposure or fine lines will be concerns of the past. In fact, <a>laser skin therapy</a> is a unique and innovative way to enjoy youthful and healthy skin without resorting to painful and inconvenient surgery. Both men and women are receiving benefits from laser skin therapy.</p>
    <p>The literature contains ample scientific evidence to support laser skin renewal. After this therapy, your skin will produce collagen, which reduces and minimizes the appearance of fine lines and wrinkles. Imagine getting all this with minimal pain and no downtime? Doesn't it make you feel like getting in touch with our laser skin specialist today?</p>
    <ul class="topic-links">
      <li><a>Laser Skin Renewal is Innovative and Unique</a></li>
      <li><a>How Does Laser Skin Renewal-Therapy Work?</a></li>
      <li><a>Number of Treatments</a></li>
      <li><a>Are there any Side Effects of Laser Skin Renewal Therapy?</a></li>
    </ul>
  </section>

  <h2 class="section-title" style="left:268px;top:564px">New Years Resolution Special!</h2>
  <section class="special">
    <div class="special-lead">
      <h3>Restore your youthful skin this year!</h3>
      <p>Take advantage of our laser skin renewal specials for single or multiple sessions at low pricing.</p>
    </div>
    <div class="deal" style="left:244px"><span class="count">1</span><div class="price">$199</div><div class="label">SINGLE<br>SESSION<br>DEAL</div></div>
    <div class="deal" style="left:310px"><span class="count">3</span><div class="price">$549</div><div class="label">SESSIONS<br>PACKAGE<br>DEAL</div></div>
    <div class="deal" style="left:376px"><span class="count">6</span><div class="price">$899</div><div class="label">SESSIONS<br>PACKAGE<br>DEAL</div></div>
  </section>
  <div class="special-call">Call <b>000-000-0000</b> to schedule your convenient appointment.</div>
  <div class="special-note">*Special ENDS January 3, 2015 at 5:00 PM.</div>

  <h2 class="section-title" style="left:268px;top:704px">Our Blog</h2>
  <svg class="blog-arrow" style="left:232px" width="16" height="28" viewBox="0 0 16 28"><polyline points="13,2 3,14 13,26" fill="none" stroke="var(--blue)" stroke-width="3"/></svg>
  <svg class="blog-arrow" style="left:712px" width="16" height="28" viewBox="0 0 16 28"><polyline points="3,2 13,14 3,26" fill="none" stroke="var(--blue)" stroke-width="3"/></svg>

  <article class="post" style="left:254px">
    <div class="post-image"><div class="post-date"><span>DEC</span><strong>14</strong></div></div>
    <h4>The skin supports its own ecosystems of microorganisms,</h4>
    <p>Skin plays a key role in protecting the body against pathogens[3] and excessive water loss.[4] Its other functions are insulation, temperature regulation.</p>
    <span class="read-more">READ MORE</span>
  </article>
  <article class="post" style="left:407px">
    <div class="post-image"><div class="post-date"><span>DEC</span><strong>03</strong></div></div>
    <h4>Oily skin is caused by over-active sebaceous glands</h4>
    <p>Sensation, synthesis of vitamin D, and the protection of vitamin B folates. Severely damaged skin will try to heal by forming scar tissue.</p>
    <span class="read-more">READ MORE</span>
  </article>
  <article class="post" style="left:561px">
    <div class="post-image"><div class="post-date"><span>NOV</span><strong>15</strong></div></div>
    <h4>Melanin: It is brown in color and present in the germinative zone</h4>
    <p>Its other functions are insulation, temperature regulation, sensation, synthesis of vitamin D, and the protection of vitamin B folates. Severely.</p>
    <span class="read-more">READ MORE</span>
  </article>

  <div class="appointment-head">
    <div class="small">YOUR</div>
    <div class="big">APPOINTMENT</div>
    <p>You need to be prepared when<br>visiting the clinic before and after<br>for skin rejuvenation.</p>
  </div>
  <form class="booking">
    <div class="field" style="top:6px">YOUR NAME</div>
    <div class="field" style="top:32px">EMAIL ADDRESS</div>
    <div class="field" style="top:58px">YOUR VISIT DATE</div>
    <div class="field" style="top:84px">YOUR VISIT TIME</div>
    <div class="field" style="top:110px;height:64px">MESSAGE</div>
    <div class="book-btn">BOOK MY VISIT</div>
  </form>

  <div class="newsletter">
    <p>Take advantage of our laser<br>skin renewal specials for single or<br>multiple sessions at low pricing...</p>
    <div class="join">JOIN OUR</div>
    <div class="title">NEWSLETTER</div>
  </div>
  <div class="link-us"><span>Link us on</span><i></i><i></i><i></i></div>
  <div class="footer-nav">Home / Studios / Prices / About / Jobs / Franchise / Shop / Contact</div>
  <div class="footer-copy">2015 VornaDerm - All rights reserved</div>

</div>
</body>
</html>
```